Business Card Design Project - 2 sided

We need a business card design for a card having one business on each side (ie. two businesses on one card). Would like a design that incorporates logo, tagline and normal fields (name, position, address, phone).

Would also like an allowance for small font text along the bottom (text to be determined, but less than 50 characters).

NB. Attached logo for Verbica Partners has two variations - either can be used.

www.verbicapartners.com / www.kelvarho.com

```html
<!DOCTYPE html>
<html lang="en">
<head>
<meta charset="utf-8">
<title>Verbica Partners / Kelvarho – Business Card</title>
<link href="https://fonts.googleapis.com/css2?family=PT+Sans:wght@400;700&display=swap" rel="stylesheet">
<style>
  :root {
    --backdrop: #e9e6e2;
    --card: #ffffff;
    --navy: #2c2a6b;
    --lime: #8cc63f;
    --sky: #3a8bc6;
    --ink: #3a3a3a;
    --rule: #8a8a8a;
  }
  * { margin: 0; padding: 0; box-sizing: border-box; }
  html, body { width: 1200px; height: 412px; overflow: hidden; }
  body {
    background: var(--backdrop);
    font-family: "PT Sans", sans-serif;
    position: relative;
  }
  .card {
    position: absolute;
    top: 64px;
    width: 523px;
    height: 299px;
    background: var(--card);
    overflow: hidden;
    transform: scale(0.9486);
    transform-origin: 0 0;
    box-shadow: 0 2px 6px rgba(0,0,0,0.25);
  }
  .card--verbica { left: 76px; --accent: var(--navy); }
  .card--kelvarho { left: 629px; --accent: var(--sky); }

  .card__swoosh { position: absolute; inset: 0; width: 100%; height: 100%; }

  .brand {
    position: absolute;
    left: 0;
    width: 291px;
    text-align: center;
  }
  .card--verbica .brand { top: 128px; }
  .card--kelvarho .brand { top: 118px; }
  .brand__row { display: inline-flex; align-items: center; gap: 10px; }
  .brand__dot {
    width: 26px; height: 26px; border-radius: 50%;
    background: var(--lime);
  }
  .brand__name {
    font-size: 26px;
    font-weight: 400;
    color: var(--accent);
    letter-spacing: 0.5px;
  }
  .card--kelvarho .brand__name { font-size: 40px; font-weight: 700; letter-spacing: 0; }
  .brand__tagline {
    margin-top: 10px;
    font-size: 11.5px;
    color: #222;
  }
  .card--kelvarho .brand__tagline {
    margin-top: 2px;
    font-size: 15px;
    font-weight: 700;
    color: #2b4a5e;
    padding-left: 40px;
  }

  .card__divider {
    position: absolute;
    left: 291px; top: 35px;
    width: 1px; height: 220px;
    background: var(--rule);
  }

  .details {
    position: absolute;
    left: 316px; top: 38px;
    color: var(--ink);
    font-size: 13.5px;
    line-height: 17.6px;
  }
  .details__name { font-size: 18px; font-weight: 700; color: var(--accent); margin-bottom: 10px; }
  .details__title { font-size: 13.5px; font-weight: 400; }
  .contact { list-style: none; }
  .contact li { display: flex; align-items: center; gap: 4px; }
  .contact svg { width: 10px; height: 10px; fill: #333; flex: none; }
  .address { margin-top: 10px; }
  .footnote {
    margin-top: 13px;
    font-size: 10.5px;
    line-height: 13.5px;
    letter-spacing: -0.2px;
  }
</style>
</head>
<body>

  <section class="card card--verbica" aria-label="Verbica Partners side">
    <svg class="card__swoosh" viewBox="0 0 523 299" preserveAspectRatio="none" aria-hidden="true">
      <path d="M0,203 C140,238 300,262 470,280 L0,299 Z" fill="var(--lime)"/>
      <path d="M0,238 C160,256 300,272 400,284 L523,250 L523,299 L0,299 Z" fill="var(--navy)"/>
      <path d="M0,237 C160,255 300,271 420,284" stroke="#fff" stroke-width="2.5" fill="none"/>
      <path d="M395,299 L523,254" stroke="#fff" stroke-width="2.5" fill="none"/>
    </svg>
    <div class="brand">
      <div class="brand__row"><span class="brand__name">Verbica Partners</span></div>
      <p class="brand__tagline">Website Translation and Localisation Specialist...</p>
    </div>
    <div class="card__divider"></div>
    <div class="details">
      <p class="details__name">Your Name <span class="details__title">/ Title</span></p>
      <ul class="contact">
        <li><svg viewBox="0 0 10 10"><path d="M2,0 L4,2 L3,4 Q5,6 6,7 L8,6 L10,8 L8,10 Q0,8 0,2 Z"/></svg>123-456-7890</li>
        <li><svg viewBox="0 0 10 10"><rect x="2.5" y="0" width="5" height="10" rx="1"/><rect x="3.5" y="1.5" width="3" height="4" fill="#fff"/></svg>123-456-7890</li>
        <li><svg viewBox="0 0 10 10"><rect x="0" y="4" width="10" height="6" rx="1"/><rect x="2" y="0" width="6" height="4"/></svg>123-456-7890</li>
        <li><svg viewBox="0 0 10 10"><path d="M0,2 H10 V9 H0 Z M0,2 L5,6 L10,2" stroke="#fff" stroke-width=".8"/></svg>name@website.com</li>
        <li><svg viewBox="0 0 10 10"><circle cx="5" cy="5" r="5"/><path d="M0,5 H10 M5,0 V10" stroke="#fff" stroke-width=".8"/></svg>www.verbicapartners.com</li>
      </ul>
      <p class="address">Complex name, Street name<br>City, State, zip code</p>
      <p class="footnote">xxxxxxxxxxxxxxxxxxxxxxxxxxx<br>xxxxxxxxxxxxxxxxxxxxxxxxxxx</p>
    </div>
  </section>

  <section class="card card--kelvarho" aria-label="Kelvarho side">
    <svg class="card__swoosh" viewBox="0 0 523 299" preserveAspectRatio="none" aria-hidden="true">
      <path d="M0,205 C140,238 300,262 470,280 L0,299 Z" fill="var(--lime)"/>
      <path d="M0,238 C160,256 300,272 400,284 L523,250 L523,299 L0,299 Z" fill="var(--sky)"/>
      <path d="M0,237 C160,255 300,271 420,284" stroke="#fff" stroke-width="2.5" fill="none"/>
      <path d="M395,299 L523,254" stroke="#fff" stroke-width="2.5" fill="none"/>
    </svg>
    <div class="brand">
      <div class="brand__row"><span class="brand__dot"></span><span class="brand__name">Kelvarho</span></div>
      <p class="brand__tagline">Professional SEO Services</p>
    </div>
    <div class="card__divider"></div>
    <div class="details">
      <p class="details__name">Your Name <span class="details__title">/ Title</span></p>
      <ul class="contact">
        <li><svg viewBox="0 0 10 10"><path d="M2,0 L4,2 L3,4 Q5,6 6,7 L8,6 L10,8 L8,10 Q0,8 0,2 Z"/></svg>123-456-7890</li>
        <li><svg viewBox="0 0 10 10"><rect x="2.5" y="0" width="5" height="10" rx="1"/><rect x="3.5" y="1.5" width="3" height="4" fill="#fff"/></svg>123-456-7890</li>
        <li><svg viewBox="0 0 10 10"><rect x="0" y="4" width="10" height="6" rx="1"/><rect x="2" y="0" width="6" height="4"/></svg>123-456-7890</li>
        <li><svg viewBox="0 0 10 10"><path d="M0,2 H10 V9 H0 Z M0,2 L5,6 L10,2" stroke="#fff" stroke-width=".8"/></svg>name@website.com</li>
        <li><svg viewBox="0 0 10 10"><circle cx="5" cy="5" r="5"/><path d="M0,5 H10 M5,0 V10" stroke="#fff" stroke-width=".8"/></svg>www.kelvarho.com</li>
      </ul>
      <p class="address">Complex name, Street name<br>City, State, zip code</p>
      <p class="footnote">xxxxxxxxxxxxxxxxxxxxxxxxxxx<br>xxxxxxxxxxxxxxxxxxxxxxxxxxx</p>
    </div>
  </section>

</body>
</html>
```